Designing business cards for my start-up business

The company is called Velloran. We are a start-up tech data company based in Guernsey, Channel Islands. We want the business cards to look clean, fresh and innovative, just what a tech company should be. We do not want the business cards to look corporate or too official such as a bank. I would like the front of the business card to have our logo and the tag line of "Bridging Skills". On the back will be our contact details, emails etc. However I am open to your ideas and suggestions. I have provided all our logos and a word doc of all our contact details. There are 4 directors of the business, so I want 4 versions of the same design.

Target Market(s)

Our clients are businesses of all industries. Its a broad target market.

Industry/Entity Type

Information Technology

Contact Information for Business Card

I have attached a word doc called "Business Cards info" which gives all contact details of the 4 employees for the company.

Requirements
Must have
• We must have our logo and the tag line of "Bridging Skills". This could on the front of the card and then the individuals contact details on the back. Other than that, I'm happy for the designers to come up with ideas/styles.
Nice to have
• N/A
Should not have
• I don't want the cards to look too formal or corporate. As mentioned, we are a tech start-up so we want to look innovative.

```html
<!DOCTYPE html>
<html lang="en">
<head>
<meta charset="utf-8">
<title>Velloran – Business Card</title>
<link rel="stylesheet" href="https://fonts.googleapis.com/css2?family=Oswald:wght@600&family=Roboto+Condensed:wght@400;700&family=Tinos:wght@700&display=swap">
<style>
  :root {
    --page-bg: #d3d5d5;
    --card-white: #ffffff;
    --brand-blue: #0a7cc2;
    --ink-grey: #4a4a4a;
    --ink-dark: #2b1c1c;
    --label: #f4f4f4;
  }
  * { margin: 0; padding: 0; box-sizing: border-box; }
  html, body { width: 1200px; height: 1200px; overflow: hidden; }
  body { background: var(--page-bg); position: relative; font-family: "Roboto Condensed", sans-serif; }

  .card {
    position: absolute;
    top: 394px;
    width: 536px;
    height: 353px;
    overflow: hidden;
    box-shadow: 0 2px 6px rgba(0,0,0,0.18);
  }
  .card--front { left: 33px; }
  .card--back { left: 621px; background: var(--card-white); }
  .card__art { position: absolute; inset: 0; width: 100%; height: 100%; }

  .brand {
    position: absolute;
    left: 0; right: 0;
    top: 238px;
    display: flex;
    align-items: center;
    justify-content: center;
    gap: 12px;
  }
  .brand__square { width: 20px; height: 20px; background: var(--card-white); }
  .brand__name {
    font-weight: 700;
    font-size: 22px;
    letter-spacing: 0.42em;
    color: var(--ink-dark);
  }
  .tagline {
    position: absolute;
    left: 0; right: 0;
    top: 284px;
    text-align: center;
    font-weight: 700;
    font-size: 30px;
    color: var(--card-white);
  }

  .person { position: absolute; left: 34px; top: 56px; }
  .person__name {
    font-family: "Oswald", sans-serif;
    font-weight: 600;
    font-size: 48px;
    line-height: 56px;
    color: var(--brand-blue);
    letter-spacing: -0.01em;
  }
  .person__role {
    font-weight: 700;
    font-size: 19px;
    color: var(--ink-grey);
    margin-top: 2px;
  }
  .contact {
    position: absolute;
    left: 34px; top: 196px;
    font-size: 21px;
    line-height: 30px;
    color: var(--ink-grey);
    list-style: none;
  }
  .address {
    position: absolute;
    right: 14px; top: 290px;
    text-align: right;
    font-size: 18px;
    line-height: 26px;
    color: var(--card-white);
    font-style: normal;
  }

  .side-label {
    position: absolute;
    top: 774px;
    width: 300px;
    text-align: center;
    font-family: "Tinos", serif;
    font-weight: 700;
    font-size: 32px;
    color: var(--label);
    text-shadow: 0 1px 1px rgba(0,0,0,0.25);
  }
  .side-label--front { left: 122px; }
  .side-label--back { left: 740px; }
</style>
</head>
<body>

<section class="card card--front">
  <svg class="card__art" viewBox="0 0 536 353" role="img" aria-label="Faceted low-poly pattern in coral, pink, orange and violet tones">
    <defs>
      <linearGradient id="frontWash" x1="0" y1="0" x2="1" y2="1">
        <stop offset="0" stop-color="#e9489a"/>
        <stop offset="0.3" stop-color="#f2665a"/>
        <stop offset="0.6" stop-color="#f59a70"/>
        <stop offset="0.85" stop-color="#d3a3b2"/>
        <stop offset="1" stop-color="#fbd0ad"/>
      </linearGradient>
      <linearGradient id="frontShade" x1="0" y1="1" x2="0.6" y2="0.3">
        <stop offset="0" stop-color="#6f5aa8" stop-opacity="0.85"/>
        <stop offset="1" stop-color="#c8287a" stop-opacity="0"/>
      </linearGradient>
    </defs>
    <rect width="536" height="353" fill="url(#frontWash)"/>
    <rect width="536" height="353" fill="url(#frontShade)"/>
  </svg>
  <div class="brand">
    <span class="brand__square"></span>
    <span class="brand__name">Velloran</span>
  </div>
  <p class="tagline">Bridging Skills</p>
</section>

<section class="card card--back">
  <svg class="card__art" viewBox="0 0 536 353" aria-hidden="true">
    <defs>
      <linearGradient id="backWash" x1="0" y1="0" x2="0.7" y2="1">
        <stop offset="0" stop-color="#f26a5b"/>
        <stop offset="0.35" stop-color="#ef6f7a"/>
        <stop offset="0.65" stop-color="#e8456a"/>
        <stop offset="0.85" stop-color="#c8287a"/>
        <stop offset="1" stop-color="#f5a27c"/>
      </linearGradient>
    </defs>
    <polygon points="286,0 536,0 536,353 219,353 326,56" fill="url(#backWash)"/>
    <polygon points="150,353 536,348 536,353" fill="#7a5aa8"/>
  </svg>
  <div class="person">
    <h1 class="person__name">Elise Tanguy</h1>
    <p class="person__role">DIRECTOR</p>
  </div>
  <ul class="contact">
    <li>www.velloran.gg</li>
    <li>Elise.Tanguy@velloran.gg</li>
    <li>44 7700 900 318</li>
  </ul>
  <address class="address">
    18A Rue des Vaux, St Peter Port,<br>
    Guernsey, GY1 4ZZ, Channel Islands
  </address>
</section>

<p class="side-label side-label--front">FRONT</p>
<p class="side-label side-label--back">BACK</p>

</body>
</html>
```